Vantler Helps - Pellbrook Gives Advertising Flyer

We are a vantler club that has received funding to run a community food drive project. We need a flyer for our community project that stands out . Our community project is trying to obtain non- perishable food for low income families and the vulnerable from residents in the area.
This flyer will be need to be visible and posted on store front windows and anywhere else where local residents can see it and be informed about the project. We will need a high quality version to print and a PDF version that will be e-mailed for promotional activities.

Target Market(s)

Community

Font styles to use
Sans Serif

Requirements
Must have
• My project must have logos as specified.
Nice to have
• - Images
- eye catching and modern

```html
<!DOCTYPE html>
<html lang="en">
<head>
<meta charset="utf-8">
<title>Vantler Helps – Pellbrook Gives Flyer</title>
<link href="https://fonts.googleapis.com/css2?family=Montserrat:wght@400;600;700;800&family=Kaushan+Script&display=swap" rel="stylesheet">
<style>
  :root {
    --backdrop: #333333;
    --paper: #ffffff;
    --sun: #f9c043;
    --ink: #111111;
    --navy: #1f4e9c;
    --berry: #a0174a;
    --teal: #1d6b6b;
    --muted: #444444;
  }
  * { box-sizing: border-box; margin: 0; padding: 0; }
  html, body { width: 1200px; height: 1105px; overflow: hidden; background: var(--backdrop); }
  body { font-family: "Montserrat", sans-serif; color: var(--ink); }

  .flyer {
    position: absolute; left: 230px; top: 30px;
    width: 740px; height: 1045px;
    background: var(--paper); overflow: hidden;
  }

  .brand { position: absolute; left: 50px; top: 52px; display: flex; align-items: center; gap: 12px; z-index: 3; }
  .brand-dot { width: 40px; height: 40px; border-radius: 50%; background: var(--sun); flex: none; }
  .brand-name { font-weight: 700; font-size: 20px; line-height: 1.15; color: var(--navy); letter-spacing: .5px; }
  .brand-url { font-size: 10px; color: var(--muted); margin-top: 4px; }

  .topic-band {
    position: absolute; left: 0; top: 150px; width: 100%; height: 80px;
    background: var(--sun); z-index: 1;
  }
  .topic-band p { position: absolute; left: 60px; top: 18px; font-size: 17px; line-height: 1.3; color: var(--ink); }

  .hero-photo {
    position: absolute; left: 400px; top: 0; width: 300px; height: 600px;
    background: linear-gradient(180deg, #f3e7df 0%, #8fa9cf 30%, #c9a57c 60%, #b8936a 100%);
    z-index: 2;
  }

  .headline-you {
    position: absolute; left: 48px; top: 262px;
    font-weight: 800; font-size: 128px; line-height: 1; color: var(--sun); letter-spacing: -3px;
  }
  .headline-tag {
    position: absolute; left: 80px; top: 405px;
    font-family: "Kaushan Script", cursive; font-size: 46px; line-height: 1.1; color: var(--ink);
  }
  .headline-tag span { display: block; padding-left: 28px; }

  .appeal-block { position: absolute; left: 0; top: 0; width: 740px; height: 1045px; z-index: 3; }

  .appeal {
    position: absolute; left: 60px; top: 690px; width: 620px; z-index: 4;
    font-size: 15px; line-height: 1.35;
  }
  .appeal h2 { font-weight: 800; font-size: 21px; margin-bottom: 18px; }
  .appeal p { margin-bottom: 14px; }
  .appeal strong { font-weight: 800; }
  .appeal .thanks { font-weight: 800; font-size: 16px; }

  .supporters {
    position: absolute; left: 50px; right: 50px; bottom: 40px;
    display: flex; align-items: flex-end; justify-content: space-between; z-index: 4;
  }
  .supporter-lead { font-size: 11px; color: var(--muted); margin-bottom: 6px; }
  .supporter-name { font-weight: 700; font-size: 17px; color: var(--navy); }
  .supporter-bank { font-weight: 700; font-size: 16px; color: var(--berry); }
  .supporter-council { font-weight: 700; font-size: 15px; color: var(--teal); }
  .supporter-fund { display: flex; align-items: center; gap: 8px; font-weight: 700; font-size: 16px; color: var(--navy); }
  .supporter-fund span { width: 20px; height: 20px; border-radius: 50%; background: var(--sun); }
</style>
</head>
<body>
  <main class="flyer">
    <div class="hero-photo" role="img" aria-label="Smiling volunteer holding a brown paper bag printed with a yellow heart"></div>

    <div class="topic-band">
      <p>Food security and the COVID<br>Crisis in Harwick Vale</p>
    </div>

    <header class="brand">
      <div class="brand-dot"></div>
      <div>
        <div class="brand-name">VANTLER HELPS<br>PELLBROOK GIVES</div>
        <div class="brand-url">www.vhpg.org.au</div>
      </div>
    </header>

    <h1 class="headline-you">YOU</h1>
    <p class="headline-tag">can make<span>a difference.</span></p>

    <svg class="appeal-block" viewBox="0 0 740 1045" aria-hidden="true">
      <polygon points="0,660 740,570 740,850 0,930" fill="var(--sun)"/>
    </svg>

    <section class="appeal">
      <h2>Can you help refill Hearthside's Food Pantry?</h2>
      <p><strong>We need donations of non – perishable food items.</strong> Look out for our bags and information in your letter box.</p>
      <p><strong>Hearthside</strong> exists to address the immediate food insecurity of vulnerable individuals and families in the Harwick Vale area.</p>
      <p class="thanks">Thank you for your support!</p>
    </section>

    <footer class="supporters">
      <div>
        <div class="supporter-lead">Proudly supported by</div>
        <div class="supporter-name">Vantler Harwick</div>
      </div>
      <div class="supporter-bank">Kestrel Bank</div>
      <div class="supporter-council">Harwick Vale</div>
      <div class="supporter-fund">The Vantler Fund <span></span></div>
    </footer>
  </main>
</body>
</html>
```